Website Design for Kelvora Cloud As a Service

We are building a service to allow customers to own their own private clouds easily and cheaply. Owning your own private cloud saves costs, and offers more flexibility than a public cloud provider but has historically been a complex and expensive option.

We plan to offer a service where we build and maintain your own private cloud on your own hardware for a cheap monthly costs. Similar to this service - https://nimbarvo.com/solutions/private-cloud

We already have a logo and branding in place - we'd like a website design to be tailored from this branding, see attached logo design.

Feel free to add important elements on the home page such as testimonials, client/partner logos, contact form, social media, etc using placeholder contents in addition to the document we attached.

We also plan to add sub-pages in the future so please make sure that your website design has a full navigation menu.

An example of the site we like: https://www.vosketri.com/ we'd be happy for you to take inspiration from this website.

Target Market(s)

B2B focused, we are targeting start-up/small/medium sized companies who needs help with their cloud and IT infrastructure.

Industry/Entity Type

IT

Number of Pages Required

1 page

Font styles to use
Other font styles liked:
• Please refer to the attachment - font must have Mayeka Demi Bold & Retroica

Requirements
Must have
• Please add placeholder menu since we're planning to have subpages later on.

```html
<!DOCTYPE html>
<html lang="en">
<head>
<meta charset="utf-8">
<title>Kelvora Cloud as a Service</title>
<link rel="stylesheet" href="https://fonts.googleapis.com/css2?family=Lexend:wght@400;500;600&family=Mulish:wght@400;600;700;800&display=swap">
<style>
:root{
  --navy:#1d3f7a;
  --blue:#1f86cf;
  --blue-dark:#1668a8;
  --sky:#eef5fc;
  --sky-2:#e4eff9;
  --text:#33425a;
  --muted:#56637a;
  --line:#dbe5ef;
  --white:#ffffff;
}
*{box-sizing:border-box;margin:0;padding:0}
html,body{width:1200px;height:4796px;overflow:hidden}
body{position:relative;background:var(--white);font-family:"Mulish",sans-serif;color:var(--text);font-size:14px;line-height:1.75}
.abs{position:absolute}
h1,h2,h3{font-family:"Lexend",sans-serif;color:var(--navy);font-weight:600}
.btn{position:absolute;display:flex;align-items:center;justify-content:center;background:var(--blue);color:var(--white);border-radius:24px;font-family:"Mulish",sans-serif;font-weight:700;font-size:15px;height:44px;z-index:2}

/* header + hero */
.hero-bg{left:0;top:0;width:1200px;height:780px;background:linear-gradient(180deg,#f3f8fd 0%,var(--sky) 100%)}
.hero-curve{left:0;top:680px;width:1200px;height:120px}
.brand{display:flex;align-items:center;gap:12px}
.brand-mark{width:52px;height:52px;border-radius:50%;background:var(--blue)}
.brand-name{font-family:"Lexend",sans-serif;font-size:44px;font-weight:500;color:var(--navy);line-height:1}
.brand-tag{font-family:"Lexend",sans-serif;font-size:17px;font-weight:500;color:var(--navy);letter-spacing:1px;text-align:right;line-height:1.1}
.nav{top:46px;left:788px;display:flex;gap:26px;font-size:14px;color:var(--navy);font-weight:600}
.hero h1,.hero .lede,.hero .cta-line{z-index:2}
.hero h1{left:43px;top:200px;width:480px;font-size:30px;line-height:1.25}
.hero .lede{left:43px;top:328px;width:430px;font-size:13.5px}
.hero .cta-line{left:43px;top:418px;width:380px;font-size:13px;color:var(--navy);font-weight:800}
.hero-art{left:540px;top:100px;width:600px;height:570px;border-radius:40px;background:radial-gradient(ellipse at 55% 50%,#4f88d6 0%,#2d62b4 38%,#b9d2ef 70%,rgba(238,245,252,0) 100%);z-index:1}

/* benefits */
.section-title{font-size:34px;line-height:1.2;text-align:center}
.benefit{position:absolute;width:240px;text-align:center}
.benefit .ico{display:block;margin:0 auto 12px;width:56px;height:56px}
.benefit h3{font-family:"Mulish",sans-serif;font-size:14.5px;font-weight:800;color:var(--navy);line-height:1.5;margin-bottom:8px}
.benefit p{font-size:13px;color:var(--muted);line-height:1.8}
.photo{border-radius:12px;background:linear-gradient(135deg,#2b3f60 0%,#3f6ea5 45%,#8eb4dc 100%)}
.deco-hand{left:640px;top:1150px;width:560px;height:400px;background:radial-gradient(ellipse at 70% 45%,rgba(125,160,205,.35) 0%,rgba(180,205,232,.2) 45%,rgba(255,255,255,0) 72%)}
.demo{left:795px;top:1008px;width:170px;height:44px;font-size:15px;gap:8px}

/* transformation */
.transform h2{left:655px;top:1560px;width:502px;font-size:34px;line-height:1.18;text-align:center}
.transform .copy{left:656px;top:1658px;width:500px;font-size:13.5px}
.transform .copy p{margin-bottom:10px}
.check{position:absolute;display:flex;align-items:center;gap:14px;font-weight:800;color:var(--navy);font-size:16px}
.check svg{width:42px;height:42px}

/* public cloud */
.card{position:absolute;top:2310px;width:351px;height:228px;background:#f4f8fc;border-radius:10px;padding:28px 26px}
.card .head{display:flex;gap:14px;align-items:center;font-weight:800;color:var(--navy);font-size:14.5px;line-height:1.5;margin-bottom:14px}
.card .head svg{flex:none;width:42px;height:42px}
.card p{font-size:12.5px;color:var(--muted);line-height:1.95}

/* difference */
.diff h2{left:43px;top:2766px;font-size:34px}
.diff ul{position:absolute;left:43px;top:2828px;width:440px;list-style:none}
.diff li{position:relative;padding-left:18px;font-size:13.5px;line-height:1.8;margin-bottom:21px}
.diff li::before{content:"";position:absolute;left:0;top:9px;width:7px;height:7px;border-radius:50%;background:var(--blue)}

/* trusted */
.trusted-bg{left:0;top:3395px;width:1200px;height:262px;background:var(--sky)}
.trusted h2{left:0;top:3428px;width:1200px;text-align:center;font-size:26px}
.partner{position:absolute;top:3515px;width:220px;display:flex;flex-direction:column;align-items:center;gap:8px}
.partner .sq{width:38px;height:38px;border-radius:6px;background:#8d94a0}
.partner .nm{font-family:"Lexend",sans-serif;font-size:30px;font-weight:400;color:#6f7784;line-height:1}
.partner .sl{font-size:12px;color:#8d94a0;letter-spacing:1px}

/* testimonial */
.quote-mark{left:550px;top:3660px;width:100px;height:70px}
.testi h3{left:0;top:3712px;width:1200px;text-align:center;font-size:21px}
.testi p{left:370px;top:3752px;width:460px;text-align:center;font-size:13.5px;line-height:1.9}
.testi .who{left:0;top:3868px;width:1200px;text-align:center;font-size:13.5px;line-height:1.6}
.dots{left:540px;top:3936px;display:flex;gap:22px}
.dots span{width:13px;height:13px;border-radius:50%;border:2px solid var(--blue)}
.dots span.on{background:var(--blue)}

/* contact + footer */
.foot-bg{left:0;top:4150px;width:1200px;height:646px;background:var(--sky)}
.contact-card{left:424px;top:4055px;width:354px;height:412px;background:var(--white);border-radius:6px;box-shadow:0 4px 18px rgba(29,63,122,.12);padding:36px 30px 0}
.contact-card h2{text-align:center;font-size:22px;font-weight:500;margin-bottom:22px}
.field{height:36px;border:1px solid var(--line);border-radius:3px;margin-bottom:12px;padding:0 14px;font-size:12px;color:#8a94a5;display:flex;align-items:center}
.field.msg{height:124px;align-items:flex-start;padding-top:10px}
.contact-card .btn{position:static;width:100%;height:40px;border-radius:20px;margin-top:14px}
.info{left:43px;display:flex;gap:14px;font-size:12px;line-height:1.5;color:var(--text)}
.info svg{width:16px;height:16px;flex:none;margin-top:2px}
.social{left:480px;top:4510px;display:flex;gap:36px}
.social span{width:34px;height:34px;border-radius:50%;background:var(--blue)}
.fcol{position:absolute;top:4508px;font-size:12.5px;line-height:2}
.fcol b{display:block;font-weight:600;color:#7a8598;letter-spacing:.5px;margin-bottom:6px}
.fcol a{display:block;color:var(--text);text-decoration:none}
.copyright{left:0;top:4760px;width:1200px;text-align:center;font-size:11px}
</style>
</head>
<body>

<!-- Hero -->
<div class="abs hero-bg"></div>
<svg class="abs hero-curve" viewBox="0 0 1200 120" preserveAspectRatio="none" aria-hidden="true"><path d="M0 20 Q600 140 1200 20 L1200 120 L0 120 Z" fill="#fff"/></svg>

<header>
  <div class="abs brand" style="left:43px;top:26px">
    <span class="brand-mark"></span>
    <div><div class="brand-name">Kelvora Cloud</div><div class="brand-tag">AS A SERVICE</div></div>
  </div>
  <nav class="abs nav"><span>Products</span><span>Solutions</span><span>Pricing</span><span>Resources</span><span>About</span></nav>
</header>

<section class="hero">
  <div class="abs hero-art" role="img" aria-label="Isometric illustration of a laptop with a cloud upload symbol, server blocks and a code window"></div>
  <h1 class="abs">A groundbreaking way for your small business to benefit from the power of the cloud</h1>
  <p class="abs lede">Kelvora Cloud as a Service is here to help small businesses utilise the power of the cloud without complicated set-ups or scary price tags.</p>
  <p class="abs cta-line">Ready to modernise your infrastructure with a fully managed private cloud solution from KCaaS?</p>
  <div class="btn" style="left:43px;top:486px;width:170px">Contact us</div>
</section>

<!-- Benefits -->
<section class="benefits">
  <h2 class="abs section-title" style="left:43px;top:832px;width:450px">How KCAAS benefits your business</h2>

  <div class="benefit" style="left:30px;top:950px">
    <svg class="ico" viewBox="0 0 56 56"><circle cx="28" cy="28" r="27" fill="#1f86cf"/><path d="M20 30a8 8 0 0 1 14-8M36 26a8 8 0 0 1-14 8" stroke="#fff" stroke-width="3" fill="none" stroke-linecap="round"/></svg>
    <h3>Totally flexible</h3><p>get the cloud you want and the latest innovations you need</p>
  </div>
  <div class="benefit" style="left:286px;top:950px">
    <svg class="ico" viewBox="0 0 56 56"><circle cx="28" cy="28" r="27" fill="#1f86cf"/><circle cx="28" cy="29" r="11" stroke="#fff" stroke-width="3" fill="none"/><path d="M28 29l5-5" stroke="#fff" stroke-width="3" stroke-linecap="round"/></svg>
    <h3>Faster</h3><p>our private cloud solutions outpace public clouds</p>
  </div>
  <div class="benefit" style="left:30px;top:1124px">
    <svg class="ico" viewBox="0 0 56 56"><circle cx="28" cy="28" r="27" fill="#1f86cf"/><circle cx="28" cy="28" r="12" stroke="#fff" stroke-width="3" fill="none"/><circle cx="28" cy="28" r="4" fill="#fff"/></svg>
    <h3>Greater value for money</h3><p>totally transparent pricing for no nasty month-end surprises</p>
  </div>
  <div class="benefit" style="left:286px;top:1124px">
    <svg class="ico" viewBox="0 0 56 56"><circle cx="28" cy="28" r="27" fill="#1f86cf"/><path d="M28 15a9 9 0 0 0-5 16.5V36h10v-4.5A9 9 0 0 0 28 15z" fill="#fff"/><rect x="23" y="38" width="10" height="3" fill="#fff"/></svg>
    <h3>No consultancy fees</h3><p>we'll work with you and charge set fees for everything</p>
  </div>
  <div class="benefit" style="left:30px;top:1298px">
    <svg class="ico" viewBox="0 0 56 56"><circle cx="28" cy="28" r="27" fill="#1f86cf"/><rect x="19" y="16" width="18" height="24" rx="2" fill="#fff"/><path d="M23 24h10M23 29h10M23 34h6" stroke="#1f86cf" stroke-width="2"/></svg>
    <h3>Management, monitoring and maintenance</h3><p>they're all included in your monthly price</p>
  </div>
  <div class="benefit" style="left:286px;top:1298px">
    <svg class="ico" viewBox="0 0 56 56"><circle cx="28" cy="28" r="27" fill="#1f86cf"/><path d="M18 22h7a3 3 0 1 1 6 0h7v8a3 3 0 1 0 0 6v4H18z" fill="#fff"/></svg>
    <h3>Tried and tested cloud solutions</h3><p>we'll deploy the right Stackwell solutions for your business</p>
  </div>

  <div class="abs deco-hand" role="img" aria-label="Faint image of a hand touching a glowing network of cloud icons"></div>
  <div class="abs photo" style="left:599px;top:843px;width:558px;height:380px" role="img" aria-label="Two colleagues with a tablet in front of a wall of digital cloud icons"></div>
  <div class="btn demo"><svg width="16" height="16" viewBox="0 0 16 16"><path d="M3 1l12 7-12 7z" fill="#fff"/></svg>View Demo</div>
</section>

<!-- Transformation -->
<section class="transform">
  <div class="abs photo" style="left:43px;top:1562px;width:556px;height:476px;border-radius:6px" role="img" aria-label="Colleagues with a laptop pointing at a digital data screen"></div>
  <h2 class="abs">KCAAS can drive your digital transformation today</h2>
  <div class="abs copy">
    <p>Organisations of all shapes and sizes are reaping the time and money saving benefits that the cloud brings.</p>
    <p>But for small businesses seeking to transition, managing the time and financial costs of transitioning, and knowing whether to opt for a public or private cloud can cause you to hit the pause button.</p>
    <p>KCAAS is here to help you switch on your cloud transformation in a way that works best for you. &nbsp;We deliver and support fully managed private cloud solutions that are:</p>
  </div>
  <div class="check" style="left:737px;top:1880px"><svg viewBox="0 0 42 42"><circle cx="21" cy="21" r="19" fill="none" stroke="#1f86cf" stroke-width="2.5"/><path d="M13 21l6 6 10-11" fill="none" stroke="#1f86cf" stroke-width="3" stroke-linecap="round"/></svg>Fast</div>
  <div class="check" style="left:947px;top:1880px"><svg viewBox="0 0 42 42"><circle cx="21" cy="21" r="19" fill="none" stroke="#1f86cf" stroke-width="2.5"/><path d="M13 21l6 6 10-11" fill="none" stroke="#1f86cf" stroke-width="3" stroke-linecap="round"/></svg>Easy</div>
  <div class="check" style="left:737px;top:1945px"><svg viewBox="0 0 42 42"><circle cx="21" cy="21" r="19" fill="none" stroke="#1f86cf" stroke-width="2.5"/><path d="M13 21l6 6 10-11" fill="none" stroke="#1f86cf" stroke-width="3" stroke-linecap="round"/></svg>Powerful</div>
  <div class="check" style="left:947px;top:1945px"><svg viewBox="0 0 42 42"><circle cx="21" cy="21" r="19" fill="none" stroke="#1f86cf" stroke-width="2.5"/><path d="M13 21l6 6 10-11" fill="none" stroke="#1f86cf" stroke-width="3" stroke-linecap="round"/></svg>Scalable</div>
  <div class="btn" style="left:822px;top:2023px;width:170px">Get started</div>
</section>

<!-- Public cloud -->
<section class="public">
  <h2 class="abs section-title" style="left:330px;top:2190px;width:540px">If you're using a public cloud now…</h2>
  <div class="card" style="left:43px">
    <div class="head"><svg viewBox="0 0 42 42"><circle cx="21" cy="21" r="20" fill="#1f86cf"/><circle cx="21" cy="21" r="8" fill="none" stroke="#fff" stroke-width="2.5"/></svg>You could be paying too much…</div>
    <p>Public cloud pricing structures have a habit of sneakily scaling up very quickly. With KCAAS, you'll always know what you're paying for your private cloud services.</p>
  </div>
  <div class="card" style="left:424px">
    <div class="head"><svg viewBox="0 0 42 42"><circle cx="21" cy="21" r="20" fill="#1f86cf"/><circle cx="15" cy="15" r="3" fill="#fff"/><circle cx="27" cy="15" r="3" fill="#fff"/><circle cx="15" cy="27" r="3" fill="#fff"/><circle cx="27" cy="27" r="3" fill="#fff"/></svg>You're likely not getting the benefits of full functionality…</div>
    <p>Public cloud providers cannot adopt new innovations and functions as quickly and easily as the private cloud solutions you'll get from KCAAS.</p>
  </div>
  <div class="card" style="left:806px">
    <div class="head"><svg viewBox="0 0 42 42"><circle cx="21" cy="21" r="20" fill="#1f86cf"/><rect x="15" y="13" width="12" height="16" rx="2" fill="none" stroke="#fff" stroke-width="2.5"/></svg>You'll be tied to the services your provider can provide…</div>
    <p>Public cloud pricing structures have a habit of sneakily scaling up very quickly. With KCAAS, you'll always know what you're paying for your private cloud services.</p>
  </div>
  <div class="btn" style="left:515px;top:2574px;width:170px">Let's talk</div>
</section>

<!-- Difference -->
<section class="diff">
  <h2 class="abs">The KCAAS Difference</h2>
  <ul>
    <li>We'll quickly get to grips with what your organisation needs, and deliver it via our private cloud solutions.</li>
    <li>Enjoy the ease of the public cloud, combined with the features, innovations and flexibility of the private cloud.</li>
    <li>You can focus on your core business while we support you with a dedicated cloud infrastructure.</li>
    <li>We'll create and deliver the launchpad that will take your business forward.</li>
    <li>Get the benefits of your own cloud infrastructure and reduce your operational costs</li>
    <li>Fast and easy computing, storage and network resources</li>
    <li>Managed operations from private Stackwell clouds and Podweave</li>
    <li>We'll support your growth and scale your cloud as you need it.</li>
  </ul>
  <div class="abs photo" style="left:599px;top:2773px;width:558px;height:478px;border-radius:6px;background:linear-gradient(150deg,#1f3552 0%,#6f9cc8 45%,#d4e4f2 100%)" role="img" aria-label="Hand touching a tablet screen in blue light"></div>
</section>

<!-- Trusted -->
<section class="trusted">
  <div class="abs trusted-bg"></div>
  <h2 class="abs">Trusted By</h2>
  <div class="partner" style="left:92px"><span class="sq"></span><span class="nm">norvant</span><span class="sl">company slogan</span></div>
  <div class="partner" style="left:356px"><span class="sq"></span><span class="nm">quelbit</span><span class="sl">company tagline</span></div>
  <div class="partner" style="left:630px"><span class="sq"></span><span class="nm">marrowline</span><span class="sl">tagline here</span></div>
  <div class="partner" style="left:890px"><span class="sq"></span><span class="nm">pexaro</span><span class="sl">awesome slogan</span></div>
</section>

<!-- Testimonial -->
<section class="testi">
  <svg class="abs quote-mark" viewBox="0 0 100 70" aria-hidden="true"><path d="M10 60V35Q10 10 40 5v12Q25 20 25 35h15v25zM55 60V35Q55 10 85 5v12Q70 20 70 35h15v25z" fill="#eef3f8"/></svg>
  <h3 class="abs">Great service, professional support</h3>
  <p class="abs">Lorem ipsum dolor sit amet, consectetuer adipiscing elit. Aenean commodo ligula eget dolor. Aenean massa. Cum sociis natoque penatibus et magnis dis parturient montes, nascetur ridiculus mus. Donec quam felis, ultricies nec, pellentesque eu, pretium quis, sem.</p>
  <div class="abs who">Dana Mercer<br>Chief Engineer</div>
  <div class="abs dots"><span class="on"></span><span></span><span></span><span></span></div>
</section>

<!-- Contact + footer -->
<div class="abs foot-bg"></div>
<form class="abs contact-card">
  <h2>Contact Us</h2>
  <div class="field">* First Name</div>
  <div class="field">* Last Name</div>
  <div class="field">* Email</div>
  <div class="field msg">Message ...</div>
  <div class="btn">Send Message</div>
</form>

<footer>
  <div class="abs info" style="top:4506px"><svg viewBox="0 0 16 16"><path d="M8 1a5 5 0 0 0-5 5c0 4 5 9 5 9s5-5 5-9a5 5 0 0 0-5-5zm0 7a2 2 0 1 1 0-4 2 2 0 0 1 0 4z" fill="#33425a"/></svg><span>88 Harborlight Lane, Millbrook,<br>MO, 65000</span></div>
  <div class="abs info" style="top:4558px"><svg viewBox="0 0 16 16"><rect x="1" y="3" width="14" height="10" rx="1" fill="#33425a"/><path d="M1 4l7 5 7-5" stroke="#fff" fill="none"/></svg><span>hello@kelvora.example</span></div>
  <div class="abs info" style="top:4602px"><svg viewBox="0 0 16 16"><path d="M4 1l3 3-2 2a9 9 0 0 0 5 5l2-2 3 3-2 3C7 15 1 9 1 3z" fill="#33425a"/></svg><span>417-555-0148</span></div>

  <div class="abs social" aria-label="Social media links"><span></span><span></span><span></span><span></span></div>

  <div class="fcol" style="left:810px"><b>COMPANY</b><a>Solutions</a><a>Pricing</a><a>About</a></div>
  <div class="fcol" style="left:947px"><b>CLIENTS</b><a>Support</a><a>Testimonials</a><a>Resources</a></div>
  <div class="fcol" style="left:1087px"><b>CONTACT</b><a>Link-1</a><a>Link-2</a><a>Link-3</a></div>

  <div class="abs brand" style="left:428px;top:4680px">
    <span class="brand-mark" style="width:44px;height:44px"></span>
    <div><div class="brand-name" style="font-size:38px">Kelvora Cloud</div><div class="brand-tag" style="font-size:15px">AS A SERVICE</div></div>
  </div>
  <div class="abs copyright">©2022 KCAAS All rights reserved.</div>
</footer>

</body>
</html>
```